Willowmere Spa and Beauty Ltd. (Name of business)

I need a business card designed for this new company based out of Toronto Ontario. We specialize in Eyelash Extensions, Manicures and Pedicures, body waxing, massages, laser hair removal and botox treatments. Also offer a variety of products for sale, such as skin cream serums, collagen gel, eye cream, etc. It is a safe relaxing and non-judgemental environnment. Clients are welcome to come be pampered for the half or full day. Many service packages to choose from.

Open 7days per week from 8am to 8pm.

Priscilla Dunmore
Spa Facilitator
Willowmere Spa and Beauty Ltd.
7200 Harcourt St; Suite 1400
Toronto ON K2P 9W4

OFFICE: 416.790.4100
FAX: 416.790.4101
CELL: 416.632.1987
EMAIL: priscilla.dunmore@willowmerespa.com

Target Market(s)

Target market is primarily female ranging from 16 years old to 50 years old.

Industry/Entity Type

Business

Contact Information for Business Card

Priscilla Dunmore
Spa Facilitator
7200 Harcourt St; Suite 1400
Toronto ON K2P 9W4

OFFICE: 416.790.4100
FAX: 416.790.4101
CELL: 416.632.1987

Logo Text

I dont have a logo yet. I would like it simple but sophisticated and modern.

Font styles to use
Serif

Requirements
Must have
• all pertinent details such as company name, logo, name and contact information, services that are offered, including package rates
Nice to have
• Company name and logo prominent. A card that is neat and the information such as address, phone number, fax, email, etc is not too crowded but laid out in an easy to read format.
• Possibly on the back of card - some of the services offered could be listed, as well as professional cream lotions and serums. Hours of operation etc.

```html
<!DOCTYPE html>
<html lang="en">
<head>
<meta charset="utf-8">
<title>Willowmere Spa and Beauty Ltd. – Business Card</title>
<link rel="stylesheet" href="https://fonts.googleapis.com/css2?family=Tinos:ital,wght@0,400;0,700;1,400&family=Arimo:wght@500&display=swap">
<style>
  :root {
    --page-bg: #ebe7e9;
    --plum-light: #93618f;
    --plum-dark: #7a4775;
    --cream: #f4eef0;
    --ornament: rgba(245, 236, 240, 0.55);
    --name-purple: #8a3d88;
    --title-pink: #d27aa9;
    --body-purple: #7b3f7a;
    --paper: #f6f3f3;
    --blossom-light: #eadbe6;
    --blossom-dark: #d6b3cc;
    --band-pink: #c97ea7;
    --band-text: #fbf2f6;
  }
  * { margin: 0; padding: 0; box-sizing: border-box; }
  html, body { width: 1200px; height: 1200px; overflow: hidden; background: var(--page-bg); }
  .canvas { position: relative; width: 1200px; height: 1200px; }

  .card {
    position: absolute;
    box-shadow: 0 6px 14px rgba(0,0,0,0.18);
    overflow: hidden;
  }

  /* Front */
  .card-front {
    left: 102px; top: 156px; width: 654px; height: 372px;
    background: linear-gradient(160deg, var(--plum-light), var(--plum-dark));
  }
  .ornament { position: absolute; }
  .ornament-top-right { right: 18px; top: 10px; width: 256px; height: 156px; }
  .ornament-bottom-left { left: 14px; top: 205px; width: 258px; height: 155px; }
  .brand-mark {
    position: absolute; left: 248px; top: 107px;
    width: 150px; height: 150px; border-radius: 50%;
    background: radial-gradient(circle at 45% 40%, #fbf8f8, #e9e1e4);
  }
  .brand-name {
    position: absolute; left: 0; right: 0; top: 263px;
    text-align: center;
    font-family: "Tinos", serif; font-size: 24px; color: var(--cream);
  }

  /* Back */
  .card-back {
    left: 464px; top: 642px; width: 652px; height: 374px;
    background: var(--paper);
  }
  .blossom-panel { position: absolute; left: 0; top: 0; width: 200px; height: 374px; }
  .holder-name {
    position: absolute; left: 222px; top: 8px;
    font-family: "Tinos", serif; font-weight: 700; font-size: 32px; color: var(--name-purple);
  }
  .holder-title {
    position: absolute; left: 235px; top: 53px;
    font-family: "Tinos", serif; font-size: 22px; color: var(--title-pink);
  }
  .address {
    position: absolute; left: 222px; top: 110px;
    font-family: "Tinos", serif; font-size: 19px; line-height: 27.5px; color: var(--body-purple);
  }
  .contacts {
    position: absolute; left: 222px; top: 209px;
    font-family: "Tinos", serif; font-style: italic; font-size: 19px; line-height: 28px; color: var(--body-purple);
    border-collapse: collapse;
  }
  .contacts td { padding: 0; }
  .contacts .label { width: 88px; }
  .contacts .email { font-size: 17.5px; }
  .hours-band {
    position: absolute; left: 164px; right: 0; top: 335px; height: 36px;
    background: var(--band-pink);
    font-family: "Arimo", sans-serif; font-weight: 500; font-size: 19px; color: var(--band-text);
    line-height: 36px; padding-left: 49px;
  }
</style>
</head>
<body>
<div class="canvas">

  <section class="card card-front">
    <svg class="ornament ornament-top-right" viewBox="0 0 256 156" role="img" aria-label="Ornamental filigree corner flourish">
      <path d="M0 10 Q120 0 250 2 Q256 80 248 156 Q230 90 180 50 Q100 20 0 10 Z" fill="var(--ornament)"/>
    </svg>
    <svg class="ornament ornament-bottom-left" viewBox="0 0 258 155" role="img" aria-label="Ornamental filigree corner flourish">
      <path d="M6 0 Q26 70 80 105 Q160 140 258 145 Q130 156 4 152 Q0 80 6 0 Z" fill="var(--ornament)"/>
    </svg>
    <div class="brand-mark"></div>
    <div class="brand-name">Willowmere Spa &amp; Beauty Ltd.</div>
  </section>

  <section class="card card-back">
    <svg class="blossom-panel" viewBox="0 0 200 374" preserveAspectRatio="none" role="img" aria-label="Soft hibiscus flower pattern">
      <defs>
        <linearGradient id="blossomFade" x1="0" y1="0" x2="1" y2="1">
          <stop offset="0" stop-color="var(--blossom-dark)"/>
          <stop offset="1" stop-color="var(--blossom-light)"/>
        </linearGradient>
      </defs>
      <path d="M0 0 H192 Q175 60 188 150 Q200 240 164 374 H0 Z" fill="url(#blossomFade)"/>
    </svg>
    <div class="holder-name">Priscilla Dunmore</div>
    <div class="holder-title">Spa Facilitator</div>
    <address class="address" style="font-style:normal">
      Willowmere Spa and Beauty Ltd.<br>
      7200 Harcourt St; Suite 1400<br>
      Toronto ON K2P 9W4
    </address>
    <table class="contacts">
      <tr><td class="label">OFFICE</td><td>416.790.4100</td></tr>
      <tr><td class="label">FAX</td><td>416.790.4101</td></tr>
      <tr><td class="label">CELL</td><td>416.632.1987</td></tr>
      <tr><td class="label">EMAIL</td><td class="email">priscilla.dunmore@willowmerespa.com</td></tr>
    </table>
    <div class="hours-band">Open 7 days per week from 8am to 8pm</div>
  </section>

</div>
</body>
</html>
```